Sole practitioner CPA needs stationery design work

I need design art work for stationery which I can take to my printer. I require letterhead, business card, with comp's slip ,envelope. I would also like a word template in the letterhead format, as well as an email signature.
There are some professional requirements regarding the Tallywise Institute motif, and the words "Liability limited by a scheme approved under Professional Standards legislation". I have attached a mock up letterhead which shows these items

Target Market(s)

Small business owners who will expect to see a professional image

Industry/Entity Type

Business

Requirements
Must have
• Must have TWI logo and the words "Liability limited by a scheme approved under Professional Standards Legislation".
Nice to have
• I have attached a 'sample" that has the logo and the words. But the sample scheme is not important.

```html
<!DOCTYPE html>
<html lang="en">
<head>
<meta charset="utf-8">
<title>Brennan Accounting – Stationery Set</title>
<link rel="stylesheet" href="https://fonts.googleapis.com/css2?family=Questrial&family=Roboto:wght@400;500;700&display=swap">
<style>
  :root {
    --bg-dark: #3d3d3d;
    --bg-light: #5c5c5c;
    --paper: #ffffff;
    --red: #e5432f;
    --orange: #e8782f;
    --amber: #eeac33;
    --brand-grey: #555555;
    --text: #333333;
    --muted: #8a8a8a;
    --beige: #f9e8cc;
    --badge-blue: #1c5aa0;
  }
  * { box-sizing: border-box; margin: 0; padding: 0; }
  html, body { width: 1200px; height: 1000px; overflow: hidden; }
  body {
    position: relative;
    background: radial-gradient(ellipse at 60% 40%, var(--bg-light), var(--bg-dark));
    font-family: "Roboto", Arial, sans-serif;
    color: var(--text);
  }
  .sheet { position: absolute; background: var(--paper); overflow: hidden; }
  .sheet > svg.swoosh { position: absolute; left: 0; top: 0; width: 100%; height: 100%; }
  .letterhead { left: 23px; top: 26px; width: 480px; height: 682px; }
  .card-front { left: 519px; top: 26px; width: 324px; height: 190px; }
  .card-back { left: 855px; top: 26px; width: 324px; height: 190px; }
  .envelope { left: 23px; top: 726px; width: 542px; height: 256px; }
  .invoice { left: 635px; top: 300px; width: 467px; height: 682px; }

  .brand { position: absolute; font-family: "Questrial", Arial, sans-serif; color: var(--brand-grey); }
  .brand .mark { display: block; border-radius: 50%; background: var(--orange); }
  .brand .name { display: block; white-space: nowrap; }
  .brand .tagline { display: block; color: var(--text); white-space: nowrap; }

  .contact { position: absolute; list-style: none; color: var(--brand-grey); }
  .contact li { display: flex; align-items: center; white-space: nowrap; }
  .icon { display: inline-block; border-radius: 2px; background: var(--red); flex: none; }

  /* letterhead */
  .letterhead .brand { left: 37px; top: 16px; }
  .letterhead .brand .mark { width: 40px; height: 40px; margin-left: 26px; margin-bottom: 4px; }
  .letterhead .brand .name { font-size: 13px; }
  .letterhead .brand .tagline { font-size: 8px; }
  .letterhead .contact.top { left: 347px; top: 56px; font-size: 7px; line-height: 9.5px; }
  .letterhead .contact.bottom { left: 184px; top: 647px; font-size: 6px; line-height: 9px; }
  .contact.small .icon { width: 6px; height: 6px; margin-right: 4px; }

  /* card front */
  .card-front .holder { position: absolute; right: 28px; top: 27px; text-align: left; }
  .card-front .holder .person { font-family: "Questrial", Arial, sans-serif; font-size: 15px; color: var(--red); }
  .card-front .holder .role { font-size: 8px; color: var(--brand-grey); }
  .card-front .contact { left: 30px; top: 95px; font-size: 9px; line-height: 12px; }
  .contact.mid .icon { width: 7px; height: 7px; margin-right: 6px; }
  .card-front .member-badge { position: absolute; left: 218px; top: 118px; width: 78px; height: 36px; border: 1px solid #cccccc; background: var(--paper); display: flex; }
  .card-front .member-badge .block { width: 46px; margin: 2px; background: var(--badge-blue); }
  .card-front .member-badge .seal { width: 18px; height: 18px; margin: auto; border-radius: 50%; background: var(--badge-blue); opacity: .6; }

  /* card back */
  .card-back .brand { left: 0; right: 0; top: 30px; text-align: center; }
  .card-back .brand .mark { width: 70px; height: 70px; margin: 0 auto 6px; }
  .card-back .brand .name { font-size: 19px; }
  .card-back .brand .tagline { font-size: 11px; }
  .card-back .liability { position: absolute; left: 0; right: 0; top: 161px; text-align: center; font-size: 8px; color: var(--paper); }

  /* envelope */
  .envelope .brand { left: 37px; top: 20px; }
  .envelope .brand .mark { width: 42px; height: 42px; margin-left: 26px; margin-bottom: 6px; }
  .envelope .brand .name { font-size: 13px; }
  .envelope .brand .tagline { font-size: 8px; }
  .envelope .contact { left: 37px; top: 97px; font-size: 7px; line-height: 9.5px; }

  /* invoice */
  .invoice .brand { left: 23px; top: 16px; }
  .invoice .brand .mark { width: 44px; height: 44px; margin-left: 26px; margin-bottom: 4px; }
  .invoice .brand .name { font-size: 13px; }
  .invoice .brand .tagline { font-size: 8px; }
  .invoice .doc-title { position: absolute; left: 347px; top: 30px; font-family: "Roboto", Arial, sans-serif; font-weight: 700; font-size: 20px; color: var(--muted); }
  .invoice .contact { left: 347px; top: 56px; font-size: 7px; line-height: 9.5px; }
  .invoice .rule { position: absolute; left: 23px; right: 18px; top: 92px; border-top: 1px dotted #9aa0b5; }
  .invoice .liability { position: absolute; left: 0; right: 0; top: 95px; text-align: center; font-size: 8.5px; color: var(--brand-grey); }
  .invoice .bill-label { position: absolute; left: 16px; top: 114px; font-weight: 700; font-size: 11px; color: #a3a3a3; }
  .invoice .bill-name { position: absolute; left: 16px; top: 129px; font-size: 11px; color: #111; }
  .invoice .bill-address { position: absolute; left: 16px; top: 145px; font-size: 7.5px; line-height: 9.5px; color: #111; }
  .invoice .table-head { position: absolute; left: 16px; top: 171px; width: 433px; height: 21px; display: flex; background: linear-gradient(90deg, var(--red), var(--amber)); }
  .invoice .table-head span { border-right: 1px solid rgba(255,255,255,.7); }
  .invoice .table-head span:last-child { border-right: none; flex: 1; }
  .invoice .row { position: absolute; left: 16px; width: 433px; height: 103px; background: var(--beige); }
  .invoice .total { position: absolute; left: 264px; top: 540px; width: 185px; height: 63px; background: var(--amber); }
</style>
</head>
<body>

<!-- Letterhead -->
<section class="sheet letterhead">
  <svg class="swoosh" viewBox="0 0 480 682" preserveAspectRatio="none" aria-hidden="true">
    <defs>
      <linearGradient id="lhTop" x1="0" x2="1"><stop offset="0" stop-color="#e8782f"/><stop offset="1" stop-color="#eeac33"/></linearGradient>
      <linearGradient id="lhBottom" x1="0" x2="1"><stop offset="0" stop-color="#e5432f"/><stop offset=".5" stop-color="#e8782f"/><stop offset="1" stop-color="#eeac33"/></linearGradient>
    </defs>
    <path d="M270 0 Q420 6 480 58 L480 0 Z" fill="url(#lhTop)"/>
    <path d="M0 648 Q230 700 480 662 L480 682 L0 682 Z" fill="url(#lhBottom)"/>
  </svg>
  <div class="brand">
    <span class="mark"></span>
    <span class="name">Brennan Accounting</span>
    <span class="tagline">certified practicing accountant</span>
  </div>
  <ul class="contact small top">
    <li><span class="icon"></span>+61-8-95551234</li>
    <li><span class="icon"></span>+61-8-95551235</li>
    <li><span class="icon"></span>liam@brennanaccounting.com.au</li>
  </ul>
  <ul class="contact small bottom">
    <li><span class="icon"></span>14 Marina Street, Dunsborough, WA, 6281</li>
    <li><span class="icon"></span>PO Box 412, Dunsborough, WA, 6281</li>
  </ul>
</section>

<!-- Business card front -->
<section class="sheet card-front">
  <svg class="swoosh" viewBox="0 0 324 190" preserveAspectRatio="none" aria-hidden="true">
    <defs>
      <linearGradient id="cfBottom" x1="0" x2="1"><stop offset="0" stop-color="#e5432f"/><stop offset=".55" stop-color="#e8782f"/><stop offset="1" stop-color="#eeac33"/></linearGradient>
    </defs>
    <path d="M0 168 Q160 196 324 172 L324 190 L0 190 Z" fill="url(#cfBottom)"/>
  </svg>
  <div class="holder">
    <p class="person">Liam Brennan</p>
    <p class="role">Owner/ Founder</p>
  </div>
  <ul class="contact mid">
    <li><span class="icon"></span>+61-8-95551234</li>
    <li><span class="icon"></span>+61-8-95551235</li>
    <li><span class="icon"></span>liam@brennanaccounting.com.au</li>
    <li><span class="icon"></span>14 Marina Street, Dunsborough, WA, 6281</li>
    <li><span class="icon"></span>PO Box 412, Dunsborough, WA, 6281</li>
  </ul>
  <div class="member-badge" role="img" aria-label="Tallywise Institute member badge">
    <span class="block"></span><span class="seal"></span>
  </div>
</section>

<!-- Business card back -->
<section class="sheet card-back">
  <svg class="swoosh" viewBox="0 0 324 190" preserveAspectRatio="none" aria-hidden="true">
    <defs>
      <linearGradient id="cbBottom" x1="0" x2="1"><stop offset="0" stop-color="#e5432f"/><stop offset=".5" stop-color="#e8782f"/><stop offset="1" stop-color="#eeac33"/></linearGradient>
    </defs>
    <path d="M0 122 Q150 150 324 140 L324 190 L0 190 Z" fill="url(#cbBottom)"/>
  </svg>
  <div class="brand">
    <span class="mark"></span>
    <span class="name">Brennan Accounting</span>
    <span class="tagline">certified practicing accountant</span>
  </div>
  <p class="liability">Liability limited by a scheme approved under Professional Standards Legislation</p>
</section>

<!-- Envelope -->
<section class="sheet envelope">
  <svg class="swoosh" viewBox="0 0 542 256" preserveAspectRatio="none" aria-hidden="true">
    <defs>
      <linearGradient id="evTop" x1="0" x2="1"><stop offset="0" stop-color="#e8782f"/><stop offset="1" stop-color="#eeac33"/></linearGradient>
      <linearGradient id="evBottom" x1="0" x2="1"><stop offset="0" stop-color="#e5432f"/><stop offset=".5" stop-color="#e8782f"/><stop offset="1" stop-color="#eeac33"/></linearGradient>
    </defs>
    <path d="M250 0 Q460 4 542 40 L542 0 Z" fill="url(#evTop)"/>
    <path d="M0 216 Q270 262 542 226 L542 256 L0 256 Z" fill="url(#evBottom)"/>
  </svg>
  <div class="brand">
    <span class="mark"></span>
    <span class="name">Brennan Accounting</span>
    <span class="tagline">certified practicing accountant</span>
  </div>
  <ul class="contact small">
    <li><span class="icon"></span>+61-8-95551234</li>
    <li><span class="icon"></span>+61-8-95551235</li>
    <li><span class="icon"></span>14 Marina Street, Dunsborough, WA, 6281</li>
    <li><span class="icon"></span>PO Box 412, Dunsborough, WA, 6281</li>
  </ul>
</section>

<!-- Invoice -->
<section class="sheet invoice">
  <svg class="swoosh" viewBox="0 0 467 682" preserveAspectRatio="none" aria-hidden="true">
    <defs>
      <linearGradient id="ivTop" x1="0" x2="1"><stop offset="0" stop-color="#e8782f"/><stop offset="1" stop-color="#eeac33"/></linearGradient>
      <linearGradient id="ivBottom" x1="0" x2="1"><stop offset="0" stop-color="#e5432f"/><stop offset=".5" stop-color="#e8782f"/><stop offset="1" stop-color="#eeac33"/></linearGradient>
    </defs>
    <path d="M250 0 Q410 6 467 40 L467 0 Z" fill="url(#ivTop)"/>
    <path d="M0 652 Q230 690 467 660 L467 682 L0 682 Z" fill="url(#ivBottom)"/>
  </svg>
  <div class="brand">
    <span class="mark"></span>
    <span class="name">Brennan Accounting</span>
    <span class="tagline">certified practicing accountant</span>
  </div>
  <h1 class="doc-title">INVOICE</h1>
  <ul class="contact small">
    <li><span class="icon"></span>+61-8-95551234</li>
    <li><span class="icon"></span>+61-8-95551235</li>
    <li><span class="icon"></span>liam@brennanaccounting.com.au</li>
  </ul>
  <div class="rule"></div>
  <p class="liability">Liability limited by a scheme approved under Professional Standards Legislation</p>
  <p class="bill-label">Invoice Slip To</p>
  <p class="bill-name">James Whitford</p>
  <p class="bill-address">7/118 Elm Road, Northcity<br>Pin- 0457812, CA</p>
  <div class="table-head">
    <span style="width:134px"></span><span style="width:122px"></span><span style="width:83px"></span><span></span>
  </div>
  <div class="row" style="top:202px"></div>
  <div class="row" style="top:314px"></div>
  <div class="row" style="top:426px"></div>
  <div class="total"></div>
</section>

</body>
</html>
```